Testing form re-design

I have 2 new testing forms in a very basic format, I need them updated to look similar to our other testing forms. Attached are the two new forms (Dermatology and GI) as well as a couple of our Original normal testing forms to compare them to. Needs to be in an editable PSD file incase I need to change the verbiage in the future. Also a few addendums to the Dermatology form - Need to add a form field for "Clinical Impression" as well as "Clinical History" with spaces 2 inches to handwrite next to them.

Industry/Entity Type

Healthcare

Font styles to use
Sans Serif

Colors

Designer to choose colors to be used in the design.

Requirements
Must have
• All the information on the current forms

```html
<!DOCTYPE html>
<html lang="en">
<head>
<meta charset="utf-8">
<title>Dermatology Test Requisition Form</title>
<link href="https://fonts.googleapis.com/css2?family=Poppins:wght@400;500;600;700&display=swap" rel="stylesheet">
<style>
:root{
  --bg:#c9dcef;
  --band:#c5d9ee;
  --paper:#ffffff;
  --ink:#2b2b2b;
  --line:#3a3a3a;
  --brand:#1f6fc0;
  --grey:#e4e4e4;
  --badge:#b3bfcc;
}
*{box-sizing:border-box;margin:0;padding:0}
html,body{width:1200px;height:1200px;overflow:hidden;background:var(--bg)}
body{font-family:"Poppins",sans-serif;color:var(--ink);position:relative}
.sheet{position:absolute;left:166px;top:35px;width:866px;height:1125px;background:var(--paper);box-shadow:0 2px 6px rgba(0,0,0,.25)}
.form{position:absolute;left:178px;top:47px;width:842px;height:1105px;border:1.5px solid var(--line)}
.header{position:absolute;left:178px;top:47px;width:842px;height:109px;background:var(--band);border-bottom:1.5px solid var(--line)}
.brand{position:absolute;left:10px;top:60px;font-weight:600;font-size:33px;color:var(--brand);letter-spacing:-.5px;white-space:nowrap}
.title{position:absolute;left:234px;top:8px;font-size:23px;font-weight:700;color:#2a2a2a;white-space:nowrap}
.addr{position:absolute;left:330px;top:46px;font-size:15px;font-weight:600;text-align:center;line-height:17px;width:280px}
.contact{position:absolute;left:310px;top:82px;font-size:16px;font-weight:600;white-space:nowrap;word-spacing:2px}
.badge{position:absolute;left:706px;top:28px;width:118px;height:46px;border-radius:6px;background:var(--badge)}
.t{position:absolute;font-size:10.2px;white-space:nowrap;line-height:12px}
.h{position:absolute;font-size:13.5px;font-weight:600;white-space:nowrap}
.b{font-weight:600}
.hr{position:absolute;height:0;border-top:1.2px solid var(--line)}
.vr{position:absolute;width:0;border-left:1.2px solid var(--line)}
.ul{display:inline-block;border-bottom:1px solid var(--line);height:10px;vertical-align:baseline}
.cb{display:inline-block;width:8px;height:8px;border:1px solid var(--line);margin:0 2px 0 4px;vertical-align:-1px}
.u{text-decoration:underline;font-weight:600}
.grey{position:absolute;left:599px;top:580px;width:421px;height:24px;background:var(--grey)}
.small{position:absolute;font-size:6.3px;line-height:8.6px;color:#222}
.num{font-size:19px;font-weight:600}
.clinical{position:absolute;left:604px;top:832px;font-size:10.8px;font-weight:600;line-height:36px;white-space:nowrap}
</style>
</head>
<body>
<div class="sheet"></div>
<div class="form"></div>

<header class="header">
  <div class="brand">HARBOR POINT</div>
  <div class="title">DERMATOLOGY TEST REQUISITION FORM</div>
  <div class="addr">4120 Lakeview Pkwy<br>Suite 210, Brookfield, MI 48210</div>
  <div class="contact">(248) 555-0147 &nbsp;&nbsp; www.harborpointlabs.com</div>
  <div class="badge" role="img" aria-label="Accreditation badge"></div>
</header>

<div class="vr" style="left:599px;top:156px;height:284px"></div>
<div class="hr" style="left:178px;top:365px;width:421px"></div>
<div class="hr" style="left:178px;top:402px;width:421px"></div>
<div class="vr" style="left:433px;top:402px;height:38px"></div>
<div class="hr" style="left:599px;top:296px;width:421px"></div>
<div class="hr" style="left:599px;top:349px;width:421px"></div>
<div class="hr" style="left:599px;top:402px;width:421px"></div>
<div class="hr" style="left:178px;top:440px;width:842px"></div>
<div class="hr" style="left:178px;top:472px;width:842px"></div>
<div class="vr" style="left:599px;top:472px;height:350px"></div>
<div class="hr" style="left:599px;top:552px;width:421px"></div>
<div class="hr" style="left:178px;top:822px;width:842px"></div>
<div class="hr" style="left:178px;top:946px;width:842px"></div>

<div class="h" style="left:183px;top:164px">ORDERING PHYSICIAN/LABORATORY</div>
<div class="t" style="left:186px;top:370px;font-size:11px">Physician to receive additional result report:</div>
<div class="t" style="left:186px;top:405px;font-size:11px">Physician’s Signature:</div>
<div class="t" style="left:439px;top:405px;font-size:11px">Date:</div>

<div class="h" style="left:604px;top:164px">PATIENT INFORMATION</div>
<div class="t" style="left:605px;top:187px">Name (Last, First) (Required): <span class="ul" style="width:252px"></span></div>
<div class="t" style="left:605px;top:204px">In Care of:<span class="ul" style="width:350px"></span></div>
<div class="t" style="left:605px;top:221px">Address: <span class="ul" style="width:356px"></span></div>
<div class="t" style="left:605px;top:240px">City: <span class="ul" style="width:190px"></span> &nbsp;&nbsp;State: <span class="ul" style="width:40px"></span> &nbsp;Zip: <span class="ul" style="width:76px"></span></div>
<div class="t" style="left:605px;top:258px">Assigned Sex at birth (required): <span class="cb"></span>Male <span class="cb"></span>Female &nbsp;&nbsp;&nbsp;DOB: <span class="ul" style="width:94px"></span></div>
<div class="t" style="left:605px;top:278px">Cell Phone:<span class="ul" style="width:88px"></span> &nbsp;&nbsp;Home Phone:<span class="ul" style="width:94px"></span> &nbsp;&nbsp;ID#: <span class="ul" style="width:62px"></span></div>

<div class="t" style="left:604px;top:302px"><span class="b" style="font-size:11px">Race:</span> <span class="cb"></span>Alaska Native or American Indian &nbsp;<span class="cb"></span>Asian &nbsp;&nbsp;<span class="cb"></span>Multiracial &nbsp;&nbsp;<span class="cb"></span>White</div>
<div class="t" style="left:602px;top:317px"><span class="cb"></span>Black or African American &nbsp;&nbsp;&nbsp;<span class="cb"></span>Does not wish to disclose &nbsp;&nbsp;&nbsp;<span class="cb"></span>Not provided</div>
<div class="t" style="left:602px;top:332px"><span class="cb"></span>Native Hawaiian or other Pacific Islander &nbsp;&nbsp;<span class="cb"></span>Other race</div>

<div class="t" style="left:604px;top:355px"><span class="b" style="font-size:11px">Gender Identity:</span> <span class="cb"></span>Male <span class="cb"></span>Female <span class="cb"></span>Gender nonconforming <span class="cb"></span>Transgender</div>
<div class="t" style="left:605px;top:370px">male-to-female <span class="cb"></span>Transgender female-to-male <span class="cb"></span>Does not wish to disclose</div>
<div class="t" style="left:602px;top:385px"><span class="cb"></span>Not provided <span class="cb"></span>Not applicable</div>

<div class="t" style="left:604px;top:409px"><span class="b" style="font-size:11px">Sexual Orientation:</span><span class="cb"></span>Bisexual &nbsp;<span class="cb"></span>Straight &nbsp;<span class="cb"></span>Gay or Lesbian &nbsp;&nbsp;<span class="cb"></span>Others</div>
<div class="t" style="left:602px;top:425px"><span class="cb"></span>Does not wish to disclose &nbsp;&nbsp;&nbsp;<span class="cb"></span>Not provided &nbsp;&nbsp;<span class="cb"></span>Not applicable</div>

<div class="t" style="left:183px;top:450px"><span class="b" style="font-size:13.5px">BILLING INFORMATION</span> <span style="font-size:8.6px;font-weight:500">(Please include a copy of the front &amp; back of card.)</span> <span class="b">Billing type:</span><span class="cb"></span>Patient <span class="cb"></span>Insurance <span class="cb"></span>Client &nbsp;<span class="b">Relation:</span><span class="cb"></span>Self <span class="cb"></span>Spouse <span class="cb"></span>Dependant</div>

<div class="h" style="left:183px;top:477px">BIOPSY INFORMATION</div>
<div class="t" style="left:183px;top:498px;font-size:11.5px;font-weight:600">ICD 10 codes (required):</div>
<div class="hr" style="left:178px;top:515px;width:421px"></div>
<div class="hr" style="left:178px;top:546px;width:421px"></div>
<div class="vr" style="left:268px;top:515px;height:31px"></div>
<div class="vr" style="left:363px;top:515px;height:31px"></div>
<div class="vr" style="left:483px;top:515px;height:31px"></div>
<div class="t" style="left:183px;top:519px">Date Collected</div>
<div class="t" style="left:278px;top:519px">Time Collected</div>
<div class="t" style="left:373px;top:519px">Collected Signature</div>
<div class="t" style="left:495px;top:519px">No Vials Collected</div>
<div class="t" style="left:181px;top:547px">Type:<span class="cb"></span>Punch Biopsy <span class="cb"></span>Shave Removal (Ink) <span class="cb"></span>Shave Biopsy <span class="cb"></span>Excision (Ink)</div>
<div class="t" style="left:178px;top:560px"><span class="cb"></span>Alopecia Sections Punch Excision (Ink) <span class="cb"></span>DIF <span class="cb"></span>Currettage</div>

<div class="t" style="left:181px;top:578px;line-height:13px"><span class="num">1</span>Sites<span class="ul" style="width:140px"></span><br><span class="b">Clinical Findings</span><br><span class="cb" style="margin-left:0"></span>Nevus Atypical <span class="cb"></span>SCC <span class="cb"></span>FEP<br><span class="cb" style="margin-left:0"></span>Melanoma DBCC <span class="cb"></span>AK <span class="cb"></span>DF<br><span class="cb" style="margin-left:0"></span>SK <span class="cb"></span>DVV</div>
<div class="t" style="left:392px;top:578px;line-height:13px"><span class="num">3</span>Sites<span class="ul" style="width:155px"></span><br><span class="b">Clinical Findings</span><br><span class="cb" style="margin-left:0"></span>Nevus Atypical <span class="cb"></span>SCC <span class="cb"></span>FEP<br><span class="cb" style="margin-left:0"></span>Melanoma DBCC <span class="cb"></span>AK <span class="cb"></span>DF<br><span class="cb" style="margin-left:0"></span>SK <span class="cb"></span>DVV</div>
<div class="t" style="left:181px;top:649px;line-height:13px"><span class="num">2</span>Sites<span class="ul" style="width:140px"></span><br><span class="b">Clinical Findings</span><br><span class="cb" style="margin-left:0"></span>Nevus Atypical <span class="cb"></span>SCC <span class="cb"></span>FEP<br><span class="cb" style="margin-left:0"></span>Melanoma DBCC <span class="cb"></span>AK <span class="cb"></span>DF<br><span class="cb" style="margin-left:0"></span>SK <span class="cb"></span>DVV</div>
<div class="t" style="left:392px;top:649px;line-height:13px"><span class="num">4</span>Sites<span class="ul" style="width:152px"></span><br><span class="b">Clinical Findings</span><br><span class="cb" style="margin-left:0"></span>Nevus Atypical <span class="cb"></span>SCC <span class="cb"></span>FEP<br><span class="cb" style="margin-left:0"></span>Melanoma DBCC <span class="cb"></span>AK <span class="cb"></span>DF<br><span class="cb" style="margin-left:0"></span>SK <span class="cb"></span>DVV</div>

<div class="t u" style="left:285px;top:726px;font-size:10.5px">ANTIMICROBIAL RESISTANCE PANEL</div>
<div class="t" style="left:194px;top:743px;line-height:12.8px">KPC-Carbapenem resistance<br>NDM-Carbapenem resistance<br>VIM-Carbapenem resistance<br>IMP-Carbapenem resistance<br>qnr-Quinolone resistance<br>vanB-Vancomycin resistance</div>
<div class="t" style="left:394px;top:743px;line-height:12.8px">OXA-48-Carbapenem resistance<br>mecA/mecC-Methicilin resistance<br>CTX-M ESBL<br>sul-Sulfonamide resistance<br>vanA-Vancomycin resistance<br>dfrA-Trimethoprim resistance</div>

<div class="t" style="left:605px;top:481px">Insured’s SS#:<span class="ul" style="width:124px"></span> &nbsp;&nbsp;&nbsp;&nbsp;Insured’s DOB:<span class="ul" style="width:126px"></span></div>
<div class="t" style="left:605px;top:499px">Primary Insurance Carrier:<span class="ul" style="width:64px"></span> Medicare, Medicaid or Policy ID#:<span class="ul" style="width:46px"></span></div>
<div class="t" style="left:605px;top:517px">Claims Address:<span class="ul" style="width:326px"></span></div>
<div class="t" style="left:605px;top:536px">Employer/Group Name:<span class="ul" style="width:118px"></span> &nbsp;&nbsp;Group#:<span class="ul" style="width:120px"></span></div>
<div class="h" style="left:604px;top:557px">LOCATION OF INFECTIONS:<span class="ul" style="width:218px;margin-left:2px"></span></div>

<div class="grey"></div>
<div class="t" style="left:706px;top:583px;font-size:14px;line-height:17px"><span class="cb" style="width:18px;height:10px"></span> <span class="u">Wound/Sepsis PCR Panel</span></div>
<div class="t" style="left:938px;top:589px">Panel includes</div>

<div class="t u" style="left:781px;top:608px">BACTERIA</div>
<div class="t" style="left:612px;top:618px;line-height:12.8px">Escherichia coli<br>Streptococcus agalactiae<br>Klebsiella oxytoca<br>Staphylococcus saprophyticus<br>Pseudomonas aeruginosa<br>Staphylococcus haemolyticus<br>Enterococcus faecium<br>Enterococcus faecalis<br>Acinetobacter calcoaceticus-baumannii complex</div>
<div class="t" style="left:852px;top:618px;line-height:12.8px">Klebsiella aerogenes<br>Klebsiella pneumoniae<br>Staphylococcus aureus<br>Streptococcuspyogenes<br>Streptococcus pneumoniae<br>Streptococcus dysgalactiae<br>Staphylococcus lugdunensis<br>Staphylococcus epidermidis</div>
<div class="t u" style="left:794px;top:736px">FUNGI</div>
<div class="t" style="left:748px;top:749px;line-height:12.8px">Candida albicans<br>Fusarium solani<br>Microsporum spp</div>
<div class="t" style="left:882px;top:749px;line-height:12.8px">Candida parapsilosis<br>Trychophyton spp</div>
<div class="t u" style="left:723px;top:793px">ANTIMICROBIAL RESISTANCE</div>
<div class="t" style="left:724px;top:806px">Methicilin Resistance (MecA+C)</div>

<div class="h" style="left:183px;top:827px">OTHER TEST/PANELS:</div>
<div class="clinical">
  <div>Clinical Impression: <span class="ul" style="width:280px"></span></div>
  <div>Clinical History: <span class="ul" style="width:298px"></span></div>
</div>

<div class="small" style="left:188px;top:950px;width:820px">
  <div style="font-weight:700;font-size:7px">Physician Authorization</div>
  <div>I, the undersigned healthcare provider, acknowledge that when ordering a Urinary Tract Infection (UTI), Nail, or Wound PCR panel through Harbor Point Labs, located at 4120 Lakeview Pkwy, Suite 210, Brookfield, MI 48210, I understand and agree to the following terms:</div>
  <div style="padding-left:10px">1. &nbsp;In some or all instances, UTI, Wound, and Nail panels and their associated resistance marker tests will be forwarded to Crestline Molecular Lab for processing and analysis.</div>
  <div style="padding-left:10px">2. &nbsp;Any pathology, cytology, and thin prep specimens will be forwarded to Meadowbrook Pathology Lab for evaluation and reporting.</div>
  <div style="padding-left:10px">3. &nbsp;I understand that while the initial order is placed with Harbor Point Labs, the actual testing may be performed by partner laboratories as specified above.</div>
  <div style="padding-left:10px">4. &nbsp;I acknowledge that this referral process may affect billing procedures and timeline for results, and I accept this as standard procedure.</div>
  <div style="padding-left:10px">5. &nbsp;I confirm that I have informed my patients about this testing arrangement as appropriate and in accordance with applicable regulations.</div>
</div>
<div class="t" style="left:663px;top:1031px;font-size:7.2px;font-weight:600">Physician Signature <span class="ul" style="width:166px;height:6px"></span> &nbsp;&nbsp;&nbsp;&nbsp;Date:<span class="ul" style="width:82px;height:6px"></span></div>
<div class="small" style="left:188px;top:1039px;font-weight:700;font-size:7px">Patient Consent and Authorization</div>
<div class="small" style="left:191px;top:1057px;width:816px">I authorize the release of my medical information including test results for submission of personalized reports to my healthcare providers and insurance carrier(s). I request that payment of benefits be made to Harbor Point Labs on my behalf. If my policy does not allow for direct payment, I agree to relinquish allocated funds to Harbor Point Labs as compensation for services rendered. I acknowledge that I will be liable for deductibles, co payments and/or co insurance as detailed by my healthcare insurer. I understand that I am liable for charges not covered by my insurer. I also authorize Harbor Point Labs to appeal insurance claims on my behalf. I acknowledge the benefits, risk and limitations of this testing as described to me by a qualified healthcare provider. My insurance may not cover or pay the full amount for testing; I may be responsible for full or part of amount charged. Harbor Point Labs has my permission to bill my insurance carrier(s). Medicare Advance Beneficiary Notice: Medicare will only pay for services it determines to be reasonable and necessary. By signing this requisition, you are confirming your agreement to assume financial responsibility for these tests.</div>
<div class="t" style="left:664px;top:1134px;font-size:7.2px;font-weight:600">Patient Signature <span class="ul" style="width:176px;height:6px"></span> &nbsp;&nbsp;&nbsp;&nbsp;Date:<span class="ul" style="width:64px;height:6px"></span></div>
</body>
</html>
```